Redesign Current Opencart Site - More Calls to actions

Our current site is www.fixmyhandset.co.uk, we had it built around 18 months ago(poorly) and the site was handed over unfinished.
We had to learn basics and pay other people to get it to the useable state it is and have been using it since. We started building www.gadgetmendersdevon.com and prefer the layout of opencart.

We want to stick with opencart as the backend, but want several pages redesigning to give a better company image and also have more CTA's across the site.

Once gadgetmendersdevon is complete, we will swap the site across to replace the fixmyhandset site. Hope that makes sense.

We want the following pages redesigned:

Homepage/corporate repairs/FAQ's/Howitworks/Reviews/Contact us

we work with a lot of corporate clients but want to push our retail arm whilst still giving a strong positive image about us and our services.

We need more CTA's making people purchase from our site.
Thanks
Derek
Updates

Would like to portray a more corporate image Thanks

Target Market(s)

21-44 year olds

Coding

Coded - Design and coding required

Number of Pages Required

5+ page

Font styles to use
Other font styles liked:
• current font on banners is harabara

Colors
0592cd
acd036

Requirements
Must have
• more CTA's
• benefits of why to use our services
• Keep fonts and colours the same as above sites.

```html
<!DOCTYPE html>
<html lang="en">
<head>
<meta charset="utf-8">
<title>Quickmend Phones – Same Day Phone &amp; Tablet Repairs</title>
<link rel="stylesheet" href="https://fonts.googleapis.com/css2?family=Open+Sans:wght@400;600;700;800&display=swap">
<style>
:root{
  --blue:#0592cd;
  --blue-dark:#04719f;
  --green:#acd036;
  --green-dark:#8fb324;
  --ink:#333a40;
  --muted:#7b8590;
  --line:#e3e7ea;
  --pale:#f3f5f6;
  --footer:#eef1f3;
  --bottom:#3a4046;
  --white:#ffffff;
}
*{box-sizing:border-box;margin:0;padding:0}
html,body{width:691px;height:1200px;overflow:hidden;background:var(--white)}
body{font-family:"Open Sans",Arial,sans-serif;color:var(--ink);font-size:8px;line-height:1.35}
.page{width:691px;height:1200px;position:relative;overflow:hidden}
a{color:inherit;text-decoration:none}

/* top bar */
.topbar{height:18px;border-bottom:1px solid var(--line);display:flex;justify-content:flex-end;align-items:center;gap:10px;padding:0 18px;font-size:6.5px;color:var(--muted)}
.topbar .welcome b{color:var(--blue);font-weight:600}

/* header */
.header{height:64px;display:flex;align-items:center;justify-content:space-between;padding:0 18px}
.brand{display:flex;flex-direction:column}
.brand-row{display:flex;align-items:center;gap:6px}
.brand-dot{width:14px;height:14px;border-radius:50%;background:var(--blue)}
.brand-name{font-size:17px;font-weight:800;color:var(--blue);letter-spacing:-.3px}
.brand-tag{font-size:5.5px;color:var(--muted);margin-top:2px}
.search{display:flex;width:210px;height:16px;border:1px solid var(--line)}
.search span{flex:1;font-size:6.5px;color:var(--muted);padding:3px 6px}
.search i{width:18px;background:var(--blue)}
.basket{display:flex;align-items:center;gap:5px;font-size:6.5px;color:var(--muted)}
.basket svg{width:16px;height:16px}
.basket b{display:block;color:var(--ink);font-weight:700}

/* nav */
.nav{height:18px;background:var(--blue);display:flex;padding:0 18px}
.nav a{color:var(--white);font-size:6.5px;font-weight:700;padding:0 14px;line-height:18px;letter-spacing:.3px}
.nav a.active{background:var(--green)}

/* hero */
.hero{height:232px;position:relative;background:linear-gradient(100deg,#1c2328 0%,#2c353c 55%,#4b555c 100%);color:var(--white);overflow:hidden}
.hero-photo{position:absolute;right:50px;top:16px;width:210px;height:200px;border-radius:6px;background:radial-gradient(ellipse at 60% 45%,#9aa3aa 0%,#5c666e 45%,rgba(44,53,60,0) 75%)}
.hero-copy{position:absolute;left:70px;top:56px;width:320px}
.hero h1{font-size:21px;font-weight:800;line-height:1.12;letter-spacing:-.2px}
.hero h2{font-size:11px;font-weight:600;margin-top:5px;color:#dfe7ec}
.hero .cta-strip{display:inline-block;margin-top:9px;background:var(--blue);font-size:7.5px;font-weight:600;padding:5px 9px}
.hero .btns{display:flex;gap:6px;margin-top:9px}
.btn{display:inline-block;font-size:7px;font-weight:700;padding:5px 10px;color:var(--white);letter-spacing:.3px}
.btn-green{background:var(--green)}
.btn-blue{background:var(--blue)}
.hero-dots{position:absolute;bottom:9px;left:50%;transform:translateX(-50%);display:flex;gap:4px}
.hero-dots i{width:5px;height:5px;border-radius:50%;background:rgba(255,255,255,.45)}
.hero-dots i.on{background:var(--white)}

/* info bar */
.infobar{height:22px;border-bottom:1px solid var(--line);background:var(--pale);display:flex;align-items:center;padding:0 40px;gap:26px;font-size:6.5px;color:var(--muted)}
.infobar .lead{color:var(--blue);font-weight:700;font-size:7.5px}
.infobar .phone{display:flex;align-items:center;gap:4px;color:var(--blue);font-weight:700;font-size:9px}
.infobar .addr{display:flex;align-items:center;gap:4px}
.infobar svg{width:9px;height:9px}

/* steps */
.steps{padding-top:38px;text-align:center}
.section-title{font-size:11px;font-weight:600;color:var(--ink)}
.steps-row{display:flex;justify-content:center;align-items:flex-start;margin-top:22px}
.step{width:110px;display:flex;flex-direction:column;align-items:center}
.step-icon{width:36px;height:36px;border-radius:50%;background:var(--blue);display:flex;align-items:center;justify-content:center}
.step-icon svg{width:18px;height:18px}
.step small{font-size:6px;color:var(--muted);margin-top:6px}
.step b{font-size:7.5px;font-weight:700;color:var(--ink)}
.step p{font-size:5.5px;color:var(--muted);margin-top:3px;width:90px}
.step-arrow{width:40px;height:36px;display:flex;align-items:center}
.step-arrow svg{width:40px;height:8px}

/* products */
.products{margin-top:34px;padding:0 18px}
.products-head{display:flex;justify-content:space-between;align-items:center;border-bottom:1px solid var(--line);padding-bottom:4px}
.products-head h3{font-size:11px;font-weight:700;color:var(--green-dark)}
.products-head .arrows{font-size:9px;color:var(--muted);letter-spacing:3px}
.product-grid{display:grid;grid-template-columns:repeat(6,1fr);gap:8px;margin-top:10px}
.product{border:1px solid var(--line);padding:7px 5px 8px;text-align:center}
.product-img{height:72px;margin:0 auto;width:42px;border-radius:4px;background:linear-gradient(180deg,#3a3f44,#15191c)}
.product-img.light{background:linear-gradient(180deg,#e9e9e6,#c6c7c3)}
.product-img.wide{width:54px}
.product h4{font-size:5.5px;font-weight:600;margin-top:6px;line-height:1.3}
.product .price{font-size:7px;font-weight:700;color:var(--blue);margin-top:2px}
.product .buy{display:inline-block;margin-top:3px;background:var(--green);color:var(--white);font-size:5.5px;font-weight:700;padding:2px 7px}

/* brands */
.brands{margin:14px 18px 0;height:32px;border-top:1px solid var(--line);border-bottom:1px solid var(--line);display:flex;justify-content:space-around;align-items:center}
.brands span{font-size:8px;font-weight:700;color:#5a636b}

/* why */
.why{text-align:center;margin-top:30px}
.why-row{display:flex;justify-content:center;gap:30px;margin-top:16px}
.why-item{display:flex;align-items:center;gap:8px;text-align:left}
.why-item .pic{width:46px;height:46px;border-radius:4px}
.why-item .map{background:linear-gradient(160deg,#3b5fa8,#c9323a)}
.why-item .plane{background:linear-gradient(160deg,#e24a3b,#f2a43a)}
.why-item .badge{border-radius:50%;background:#b22a2a}
.why-item b{font-size:7.5px;font-weight:700;color:var(--blue);display:block;width:92px}

/* awards */
.awards{margin-top:34px;display:flex;justify-content:center;align-items:center;gap:22px}
.awards .shape{background:#d9dde0}
.awards .s1{width:58px;height:34px}
.awards .s2{width:80px;height:40px}
.awards .s3{width:62px;height:30px}
.awards .s4{width:36px;height:36px;border-radius:50%}
.awards .s5{width:50px;height:30px}
.awards .partner{display:flex;align-items:center;gap:4px;font-size:10px;font-weight:700;color:var(--blue)}
.awards .partner i{width:12px;height:12px;background:var(--green)}

/* footer */
.footer{position:absolute;left:0;right:0;top:996px;height:156px;background:var(--footer);padding:16px 18px 0}
.footer-cols{display:grid;grid-template-columns:repeat(5,1fr) 1.5fr;gap:10px}
.footer h5{font-size:7.5px;font-weight:700;color:var(--blue);margin-bottom:5px}
.footer li{list-style:none;font-size:6px;color:var(--muted);line-height:1.8}
.newsletter .field{height:14px;border:1px solid var(--line);background:var(--white);font-size:5.5px;color:var(--muted);padding:3px 5px;display:flex;justify-content:space-between}
.newsletter .field b{background:var(--green);color:var(--white);padding:0 4px;margin:-3px -5px -3px 0;line-height:12px;font-weight:700}
.socials{display:grid;grid-template-columns:repeat(5,14px);gap:5px;margin-top:8px}
.socials i{width:14px;height:14px;border-radius:50%;background:var(--blue)}
.socials i:nth-child(2n){background:var(--green)}
.socials i:nth-child(3n){background:#5a636b}
.footer-legal{margin-top:8px;border-top:1px solid var(--line);padding-top:7px;display:flex;justify-content:space-between;align-items:center;font-size:5.5px;color:var(--muted)}
.cards{display:flex;gap:3px}
.cards i{width:18px;height:11px;background:#cdd2d6}
.bottom{position:absolute;left:0;right:0;bottom:0;height:48px;background:var(--bottom);color:#c3c9ce;font-size:6px;display:flex;flex-direction:column;justify-content:center;padding:0 18px;gap:3px}
</style>
</head>
<body>
<div class="page">

  <div class="topbar">
    <span>My Account</span><span>Wish List</span><span>Basket</span><span>Checkout</span>
    <span class="welcome">Welcome visitor you can <b>login</b> or <b>create an account</b>.</span>
  </div>

  <header class="header">
    <div class="brand">
      <div class="brand-row"><span class="brand-dot"></span><span class="brand-name">Quickmend Phones</span></div>
      <span class="brand-tag">UK based nationwide same day phone repair specialists</span>
    </div>
    <div class="search"><span>Search</span><i></i></div>
    <div class="basket">
      <svg viewBox="0 0 16 16"><path d="M1 3h2.5l2 8h7.5l1.8-6H4.3" fill="none" stroke="#0592cd" stroke-width="1.5"/><circle cx="6.5" cy="13.5" r="1.2" fill="#0592cd"/><circle cx="12" cy="13.5" r="1.2" fill="#0592cd"/></svg>
      <span><b>Shopping Cart</b>0 item(s) - £0.00</span>
    </div>
  </header>

  <nav class="nav">
    <a class="active">HOME</a><a>CORPORATE REPAIRS</a><a>FAQS</a><a>HOW IT WORKS</a><a>REVIEWS</a><a>CONTACT US</a>
  </nav>

  <section class="hero">
    <div class="hero-photo" role="img" aria-label="Photograph of a hand holding a smartphone"></div>
    <div class="hero-copy">
      <h1>SAME DAY PHONE &amp;<br>TABLET REPAIRS</h1>
      <h2>Fast FreePost Service</h2>
      <span class="cta-strip">Get Your Device Repaired Online Today</span>
      <div class="btns"><a class="btn btn-green">BUY REPAIR</a><a class="btn btn-blue">LEARN MORE</a></div>
    </div>
    <div class="hero-dots"><i class="on"></i><i></i><i></i></div>
  </section>

  <div class="infobar">
    <span><span class="lead">Same Day Repairs Instore</span> Or use our free post service</span>
    <span class="phone"><svg viewBox="0 0 10 10"><path d="M2 1l2 2-1 1.3c.6 1.2 1.5 2.1 2.7 2.7L7 6l2 2-1.2 1.3C4.5 9 1 5.5.7 2.2z" fill="#0592cd"/></svg>01632 960418</span>
    <span class="addr"><svg viewBox="0 0 10 10"><path d="M5 .5a3.3 3.3 0 0 0-3.3 3.3C1.7 6.3 5 9.5 5 9.5s3.3-3.2 3.3-5.7A3.3 3.3 0 0 0 5 .5z" fill="#acd036"/><circle cx="5" cy="3.8" r="1.2" fill="#fff"/></svg>Unit 12, Harbour Lane, Plymouth, Devon PL4 0XX</span>
  </div>

  <section class="steps">
    <h3 class="section-title">Get Your Mobile Phone Repaired In Just Four Easy Steps</h3>
    <div class="steps-row">
      <div class="step">
        <div class="step-icon"><svg viewBox="0 0 18 18"><rect x="2" y="4" width="14" height="10" rx="1.5" fill="none" stroke="#fff" stroke-width="1.5"/><rect x="2" y="6.5" width="14" height="2" fill="#fff"/></svg></div>
        <small>Step 1</small><b>Pay Online</b>
        <p>Choose your repair and pay securely through our website</p>
      </div>
      <div class="step-arrow"><svg viewBox="0 0 40 8"><path d="M2 4h32M30 1l4 3-4 3" stroke="#acd036" stroke-width="1.5" fill="none"/></svg></div>
      <div class="step">
        <div class="step-icon"><svg viewBox="0 0 18 18"><rect x="5" y="2" width="8" height="4" fill="#fff"/><rect x="2" y="6" width="14" height="7" rx="1" fill="#fff"/><rect x="5" y="10" width="8" height="6" fill="#0592cd" stroke="#fff" stroke-width="1.2"/></svg></div>
        <small>Step 2</small><b>Print Invoice</b>
        <p>Print the invoice we email and pack it with your device</p>
      </div>
      <div class="step-arrow"><svg viewBox="0 0 40 8"><path d="M2 4h32M30 1l4 3-4 3" stroke="#acd036" stroke-width="1.5" fill="none"/></svg></div>
      <div class="step">
        <div class="step-icon"><svg viewBox="0 0 18 18"><rect x="2" y="4" width="14" height="10" rx="1" fill="none" stroke="#fff" stroke-width="1.5"/><path d="M2.5 4.5L9 10l6.5-5.5" fill="none" stroke="#fff" stroke-width="1.5"/></svg></div>
        <small>Step 3</small><b>Send by Post</b>
        <p>Post your phone to us free of charge using our label</p>
      </div>
      <div class="step-arrow"><svg viewBox="0 0 40 8"><path d="M2 4h32M30 1l4 3-4 3" stroke="#acd036" stroke-width="1.5" fill="none"/></svg></div>
      <div class="step">
        <div class="step-icon"><svg viewBox="0 0 18 18"><path d="M3.5 9.5l3.5 3.5 7.5-8" fill="none" stroke="#fff" stroke-width="2"/></svg></div>
        <small>Step 4</small><b>Receive Back</b>
        <p>We repair and return your device fast by tracked post</p>
      </div>
    </div>
  </section>

  <section class="products">
    <div class="products-head"><h3>Featured Products</h3><span class="arrows">‹ ›</span></div>
    <div class="product-grid">
      <div class="product"><div class="product-img" role="img" aria-label="Product photo of a black smartphone"></div><h4>Vista Z1<br>Screen Replacement</h4><div class="price">£49.99</div><span class="buy">Buy Now</span></div>
      <div class="product"><div class="product-img" role="img" aria-label="Product photo of a black smartphone"></div><h4>Vista Z1<br>Screen Replacement</h4><div class="price">£49.99</div><span class="buy">Buy Now</span></div>
      <div class="product"><div class="product-img wide" role="img" aria-label="Product photo of a tablet"></div><h4>Tablet 2<br>Screen Replacement</h4><div class="price">£59.99</div><span class="buy">Buy Now</span></div>
      <div class="product"><div class="product-img light" role="img" aria-label="Product photo of a silver smartphone"></div><h4>Phone 6<br>Screen Replacement</h4><div class="price">£69.99</div><span class="buy">Buy Now</span></div>
      <div class="product"><div class="product-img" role="img" aria-label="Product photo of a black smartphone"></div><h4>Vista Z1<br>Screen Replacement</h4><div class="price">£49.99</div><span class="buy">Buy Now</span></div>
      <div class="product"><div class="product-img light" role="img" aria-label="Product photo of a white smartphone"></div><h4>Vista Z1<br>Screen Replacement</h4><div class="price">£49.99</div><span class="buy">Buy Now</span></div>
    </div>
  </section>

  <div class="brands">
    <span>Corvane</span><span>Halcyra</span><span>Nordell</span><span>Pomel</span><span>Lumetra</span><span>Handset Weekly</span><span>Taviko</span>
  </div>

  <section class="why">
    <h3 class="section-title">Why to use our services</h3>
    <div class="why-row">
      <div class="why-item"><div class="pic map" role="img" aria-label="Illustrated map of the United Kingdom"></div><b>Nationwide Repair Service</b></div>
      <div class="why-item"><div class="pic plane" role="img" aria-label="Illustration of a delivery plane"></div><b>Fast Service, Free Return Delivery</b></div>
      <div class="why-item"><div class="pic badge" role="img" aria-label="Customer service award badge"></div><b>Excellent UK Based Customer Service</b></div>
    </div>
  </section>

  <div class="awards">
    <div class="shape s1" role="img" aria-label="Trade certification badge"></div>
    <div class="shape s2" role="img" aria-label="Industry awards 2014 finalist badge"></div>
    <div class="shape s3" role="img" aria-label="Business listing badge"></div>
    <div class="shape s4" role="img" aria-label="Accreditation seal"></div>
    <div class="shape s5" role="img" aria-label="Partner listing badge"></div>
    <div class="partner"><i></i>CaseTrader</div>
  </div>

  <footer class="footer">
    <div class="footer-cols">
      <div><h5>Navigation</h5><ul><li>Home</li><li>Corporate Repairs</li><li>FAQs</li><li>How it works</li><li>Reviews</li><li>Contact us</li></ul></div>
      <div><h5>Information</h5><ul><li>About Us</li><li>Delivery Information</li><li>Privacy Policy</li><li>Terms &amp; Conditions</li></ul></div>
      <div><h5>Customer Service</h5><ul><li>Contact Us</li><li>Returns</li><li>Site Map</li></ul></div>
      <div><h5>Extras</h5><ul><li>Brands</li><li>Gift Vouchers</li><li>Affiliates</li><li>Specials</li></ul></div>
      <div><h5>My Account</h5><ul><li>My Account</li><li>Order History</li><li>Wish List</li><li>Newsletter</li></ul></div>
      <div class="newsletter"><h5>Newsletter Subscribe</h5>
        <div class="field"><span>Enter your email</span><b>GO</b></div>
        <div class="socials"><i></i><i></i><i></i><i></i><i></i><i></i><i></i><i></i><i></i><i></i></div>
      </div>
    </div>
    <div class="footer-legal">
      <span>Copyright © 2015 Quickmend Phones. All rights reserved. www.quickmendphones.co.uk</span>
      <div class="cards"><i></i><i></i><i></i><i></i><i></i></div>
    </div>
  </footer>

  <div class="bottom">
    <span>Copyright © 2015 Quickmend Services Ltd. All Rights Reserved. Registered in England.</span>
    <span>Registered Office: Unit 12, Harbour Lane, Plymouth, Devon PL4 0XX · Tel: 01632 960418 · hello@quickmendphones.co.uk</span>
  </div>

</div>
</body>
</html>
```